Baby and kids clothes e-commerce website

We need a clothes ecommerce page with cart and live chat available in English and Spanish. Easy to maintain. Name of the shop is TULINDA. I need it to be really soft colour palette and easy to navigate. It needs a mobile version.

LOGO NAME "TULINDA" and there will be a very cute teddy next to it. Picture OSOMain will be the main Bear which could have different accessories such as picture attached OSOkids.

Target Market(s)

25-40 women with kids. Clothes will be quality baby and junior clothing.

Industry/Entity Type

Baby

Logo Text

TULINDA

Coding

Coded - Design and coding required

Number of Pages Required

5+ page

Requirements
Must have
• It must have a cart, a live chat, account section and newsletter sign up.
• Option to add discounts and change different flash details like in brellow.example. Also blog feature and all the social Access (including Pinterest). It also needs to have the option to add a product catalogue where products can be selected.
• It will be for baby and junior clothing.
• The 5 pages will be :
• MAIN
• BABY
• GIRLS
• BOYS
• OUTLET
• It needs to have the same pages in both English and Spanish.
Nice to have
• CART
• Account section
• Newsletter sign up
• Product catalogue section
• Discounts and vouchers
• Blog Access
• Social sites including pinterest

```html
<!DOCTYPE html>
<html lang="en">
<head>
<meta charset="utf-8">
<title>Tulinda – Baby &amp; Kids Clothing</title>
<link href="https://fonts.googleapis.com/css2?family=Baloo+2:wght@500;600;700&family=Open+Sans:wght@400;600;700&family=Pacifico&display=swap" rel="stylesheet">
<style>
:root{
  --purple:#b8a2e3;
  --purple-dark:#9d83d6;
  --teal:#6fd0cf;
  --teal-dark:#3fb8b6;
  --orange:#f5a93b;
  --orange-deep:#f37a3a;
  --pink:#e58fb0;
  --sand:#f0c878;
  --ink:#333842;
  --muted:#8a8f99;
  --line:#e6e6ea;
  --soft:#f5f5f7;
  --white:#ffffff;
  --star:#f6b93b;
}
*{box-sizing:border-box;margin:0;padding:0}
html,body{width:1200px;height:4534px;overflow:hidden}
body{position:relative;background:var(--white);font-family:"Open Sans",Arial,sans-serif;color:var(--ink);font-size:13px}
.abs{position:absolute}
.heading{font-family:"Baloo 2",Arial,sans-serif;font-weight:700;color:var(--ink)}
.photo{display:block}
.btn{display:inline-block;border-radius:20px;font-weight:700;font-size:12px;text-transform:uppercase;color:#fff;background:var(--orange);padding:8px 24px;letter-spacing:.5px}

/* header */
.site-header{top:0;left:0;width:1200px;height:75px}
.brand{position:absolute;left:196px;top:14px;display:flex;align-items:center;gap:8px}
.brand-name{font-family:"Baloo 2",Arial,sans-serif;font-weight:700;font-size:34px;color:var(--teal);letter-spacing:1px}
.brand-dot{width:18px;height:18px;border-radius:50%;background:var(--orange)}
.search{position:absolute;left:462px;top:22px;width:276px;height:30px;border-radius:16px;background:#eeeef1;display:flex;align-items:center;padding-left:16px;color:var(--muted);font-size:11px}
.search-btn{position:absolute;right:2px;top:2px;width:26px;height:26px;border-radius:50%;background:var(--purple);display:flex;align-items:center;justify-content:center}
.header-links{position:absolute;left:806px;top:28px;display:flex;gap:20px;font-size:12px;color:var(--ink);align-items:center}
.cart{display:flex;align-items:center;gap:6px}
.main-nav{top:75px;left:0;width:1200px;height:40px;background:var(--purple);display:flex;justify-content:center;gap:42px;align-items:center}
.main-nav a{color:#fff;font-weight:700;font-size:12px;text-decoration:none;letter-spacing:.5px}
.main-nav a.active{color:var(--orange)}

/* hero */
.hero{top:115px;left:0;width:1200px;height:400px;background:#f3f3f3}
.hero-kids-left{left:90px;top:10px;width:360px;height:385px;background:radial-gradient(ellipse at 50% 55%,#e8c5c0 0%,#d9dfe8 45%,#f3f3f3 75%)}
.hero-kids-right{left:710px;top:20px;width:380px;height:375px;background:radial-gradient(ellipse at 50% 55%,#f0d7c4 0%,#d7e6d0 45%,#f3f3f3 75%)}
.hero-copy{left:420px;top:80px;width:360px;text-align:center}
.hero-script{font-family:"Pacifico",cursive;color:var(--orange);font-size:28px}
.hero-script small{font-family:"Open Sans",Arial,sans-serif;font-size:13px;color:var(--muted);margin-left:4px}
.hero-title{font-family:"Baloo 2",Arial,sans-serif;font-weight:700;font-size:52px;color:var(--teal);line-height:1.1}
.hero-title span{color:var(--orange)}
.hero-copy .btn{margin-top:14px}

/* promo grid */
.promo{top:525px;left:163px;width:874px;height:430px}
.promo-tile{position:absolute;overflow:hidden}
.tile-boy{left:0;top:0;width:284px;height:430px;background:linear-gradient(160deg,#cfd8de,#9aa9b4)}
.tile-look{left:293px;top:0;width:286px;height:207px;background:linear-gradient(160deg,#c8b9a6,#8f7f6c)}
.tile-sale{left:293px;top:216px;width:286px;height:214px;background:linear-gradient(160deg,#6ea0b3,#2f5a6d)}
.tile-girl{left:588px;top:0;width:286px;height:430px;background:linear-gradient(160deg,#dde4e8,#b6c1c6)}
.badge-circle{position:absolute;width:140px;height:140px;border-radius:50%;text-align:center;color:#fff;display:flex;flex-direction:column;justify-content:center;align-items:center}
.badge-circle .age{font-size:12px;font-weight:600}
.badge-circle .big{font-family:"Baloo 2",Arial,sans-serif;font-weight:700;font-size:26px;line-height:1.05}
.tile-boy .badge-circle{left:20px;top:250px;background:var(--sand)}
.tile-girl .badge-circle{left:56px;top:250px;background:var(--teal)}
.look-strip{position:absolute;left:0;bottom:0;background:var(--teal-dark);color:#fff;font-family:"Baloo 2",Arial,sans-serif;font-weight:700;font-size:16px;padding:6px 22px}
.sale-copy{position:absolute;left:0;top:110px;width:100%;text-align:center;color:#fff}
.sale-copy .big{font-family:"Baloo 2",Arial,sans-serif;font-weight:700;font-size:30px}
.sale-copy .small{font-weight:700;font-size:13px}
.sale-tag{position:absolute;left:120px;top:40px;width:48px;height:48px;border-radius:50%;background:var(--teal);border:3px solid #fff;color:#fff;font-size:10px;font-weight:700;display:flex;align-items:center;justify-content:center}

/* section boxes */
.box{position:absolute;left:163px;width:874px;border:1px solid var(--line);background:#fff}
.box-title{position:absolute;left:0;width:100%;text-align:center;font-family:"Baloo 2",Arial,sans-serif;font-weight:700;font-size:26px}
.box-title::after{content:"";display:block;width:40px;height:2px;background:var(--orange);margin:2px auto 0}
.box-sub{position:absolute;left:0;width:100%;text-align:center;font-size:11px;color:var(--muted)}
.tabs{position:absolute;left:0;width:100%;display:flex;justify-content:center;gap:10px;font-size:11px;font-weight:600}
.tabs span{padding:5px 18px;border-radius:14px}
.tabs .on{background:var(--orange);color:#fff}

/* product card */
.product{position:absolute;width:185px;height:252px;background:#fff;text-align:center}
.product .pic{position:relative;height:160px;background:#f4f4f6;border-radius:4px;overflow:hidden}
.product .pic .photo{position:absolute;left:40px;top:18px;width:105px;height:125px;border-radius:8px}
.product .flag{position:absolute;left:0;top:0;width:0;height:0;border-top:44px solid var(--orange-deep);border-right:44px solid transparent}
.product .flag-text{position:absolute;left:3px;top:6px;color:#fff;font-size:8px;font-weight:700;transform:rotate(-45deg)}
.product .name{margin-top:14px;font-size:11px;font-weight:700;text-transform:uppercase}
.product .stars{color:var(--star);font-size:10px;letter-spacing:1px;margin-top:2px}
.product .price{font-size:11px;margin-top:8px}
.product .price s{color:var(--muted);margin-right:6px}
.product .price b{color:var(--orange-deep)}
.dots{position:absolute;left:0;width:100%;text-align:center;font-size:14px;letter-spacing:4px;color:var(--ink)}

/* deal */
.deal{top:1480px;left:163px;width:874px;height:371px}
.deal-left{position:absolute;left:0;top:0;width:500px;height:371px;background:var(--teal)}
.deal-right{position:absolute;left:500px;top:0;width:374px;height:371px;background:linear-gradient(160deg,#e7a2bc,#c96f92)}
.deal-copy{position:absolute;left:0;top:40px;width:460px;text-align:center;color:#fff}
.deal-copy .script{font-family:"Pacifico",cursive;color:var(--sand);font-size:18px}
.deal-copy .big{font-family:"Baloo 2",Arial,sans-serif;font-weight:700;font-size:40px;line-height:1.1}
.deal-copy .small{font-size:11px}
.countdown{position:absolute;left:90px;top:192px;display:flex;gap:24px}
.count{width:62px;height:62px;border-radius:50%;background:#fff;border:5px solid;display:flex;align-items:center;justify-content:center;font-family:"Baloo 2",Arial,sans-serif;font-weight:700;font-size:18px}
.deal .btn{position:absolute;left:186px;top:295px}
.pill{position:absolute;left:440px;top:30px;width:120px;height:310px;border-radius:60px;background:var(--sand);display:flex;flex-direction:column;align-items:center;justify-content:space-around;padding:14px 0}
.pill .photo{width:86px;height:86px;border-radius:50%;border:4px solid #fff;background:linear-gradient(160deg,#f3d6c4,#c9a88f)}

/* newsletter */
.newsletter{top:2582px;left:163px;width:874px;height:154px;background:var(--purple)}
.newsletter-inner{position:absolute;left:10px;top:10px;width:854px;height:134px;border:2px dashed rgba(255,255,255,.7)}
.news-title{position:absolute;left:40px;top:40px;font-family:"Pacifico",cursive;color:#fff;font-size:24px}
.news-sub{position:absolute;left:40px;top:80px;color:#fff;font-size:11px}
.news-input{position:absolute;left:360px;top:58px;width:225px;height:36px;background:#fff;font-size:11px;color:var(--muted);padding:10px 14px}
.news-btn{position:absolute;left:585px;top:58px;width:120px;height:36px;background:var(--orange);color:#fff;font-size:11px;font-weight:700;display:flex;align-items:center;justify-content:center}
.news-kid{position:absolute;left:760px;top:6px;width:100px;height:148px;border-radius:50px 50px 0 0;background:linear-gradient(180deg,#f3d3b8,#6fa2cf)}

/* categories */
.cat-title{position:absolute;left:50px;top:38px;font-family:"Baloo 2",Arial,sans-serif;font-weight:700;font-size:18px}
.cat-list{position:absolute;left:50px;top:80px;list-style:none}
.cat-list li{display:flex;align-items:center;gap:12px;font-size:11px;height:48px}
.cat-list i{width:30px;height:30px;border-radius:50%;display:block}
.arrow{position:absolute;font-size:16px;color:var(--muted)}

/* blog */
.post{position:absolute;width:270px}
.post .photo{height:160px}
.post h3{font-size:13px;font-weight:700;margin-top:16px;line-height:1.4}
.post .meta{font-size:10px;color:var(--muted);margin-top:8px;display:flex;gap:14px}
.post .meta b{color:var(--orange-deep)}
.post p{font-size:10px;color:var(--muted);margin-top:8px;line-height:1.6}

/* bottom banners */
.banner{position:absolute;top:3594px;height:356px;overflow:hidden}
.banner-copy{position:absolute;color:#fff;font-family:"Baloo 2",Arial,sans-serif;font-weight:700}
.banner-copy .script{font-family:"Pacifico",cursive;font-weight:400;font-size:24px}

/* features */
.features{top:3990px;left:0;width:1200px;height:130px}
.feature{position:absolute;width:140px;text-align:center}
.feature h4{font-size:12px;font-weight:700;margin-top:8px}
.feature p{font-size:8px;color:var(--muted);margin-top:2px}

/* footer */
.site-footer{top:4160px;left:0;width:1200px;height:310px;border-top:1px solid var(--line)}
.foot-col h5{font-size:11px;font-weight:700;text-transform:uppercase;margin-bottom:14px}
.foot-col{position:absolute;top:30px;font-size:10px;color:var(--muted);line-height:2}
.foot-field{width:194px;height:24px;border:1px solid var(--line);margin-bottom:10px;font-size:9px;padding:5px 8px;color:var(--muted)}
.social{display:flex;gap:8px;margin-top:30px}
.social i{width:12px;height:12px;border-radius:50%;background:var(--ink);display:block}
.cards{position:absolute;left:480px;top:236px;display:flex;gap:6px}
.cards i{width:38px;height:24px;border-radius:3px;display:block}
.chat-btn{position:absolute;left:836px;top:273px;width:186px;height:30px;background:#f08ca0;color:#fff;font-weight:700;font-size:12px;display:flex;align-items:center;justify-content:center;gap:8px}
.copyright{top:4470px;left:0;width:1200px;height:64px;background:var(--purple);color:#fff;font-size:11px;text-align:center;padding-top:26px}
.to-top{top:4485px;left:1128px;width:38px;height:38px;border-radius:50%;background:rgba(255,255,255,.35);display:flex;align-items:center;justify-content:center}
</style>
</head>
<body>

<header class="abs site-header">
  <div class="brand"><span class="brand-name">Tulinda</span><span class="brand-dot"></span></div>
  <div class="search">Search...
    <span class="search-btn"><svg width="12" height="12" viewBox="0 0 12 12"><circle cx="5" cy="5" r="3.5" fill="none" stroke="#fff" stroke-width="1.5"/><path d="M7.6 7.6 11 11" stroke="#fff" stroke-width="1.5"/></svg></span>
  </div>
  <div class="header-links">
    <span>My Account ▾</span><span>Eng ▾</span><span>$ ▾</span>
    <span class="cart"><svg width="16" height="14" viewBox="0 0 16 14"><path d="M1 1h2.5l2 8h8l1.5-6H4.5" fill="none" stroke="#f5a93b" stroke-width="1.6"/><circle cx="6.5" cy="12" r="1.3" fill="#f5a93b"/><circle cx="12.5" cy="12" r="1.3" fill="#f5a93b"/></svg>$0.00</span>
  </div>
</header>

<nav class="abs main-nav">
  <a class="active" href="#">HOME</a><a href="#">BABY</a><a href="#">GIRLS</a><a href="#">BOYS</a><a href="#">OUTLET</a><a href="#">BLOG</a><a href="#">CONTACT US</a>
</nav>

<section class="abs hero">
  <div class="abs photo hero-kids-left" role="img" aria-label="Two young children sitting on the floor in colourful clothes"></div>
  <div class="abs photo hero-kids-right" role="img" aria-label="Toddler girl playing with coloured building blocks"></div>
  <div class="abs hero-copy">
    <div class="hero-script">Online<small>Shopping Store</small></div>
    <div class="hero-title">Flat <span>20% Off</span></div>
    <span class="btn">Shop now</span>
  </div>
</section>

<section class="abs promo">
  <div class="promo-tile tile-boy photo" role="img" aria-label="Boy in denim jacket and cap">
    <div class="badge-circle"><span class="age">Boys 4 - 14 years</span><span class="big">Shop by<br>Look</span></div>
  </div>
  <div class="promo-tile tile-look photo" role="img" aria-label="Knitted toy accessories on a wooden table">
    <span class="look-strip">Shop by Look</span>
  </div>
  <div class="promo-tile tile-sale photo" role="img" aria-label="Children's outfits on a blue background">
    <span class="sale-tag">Sale</span>
    <div class="sale-copy"><div class="big">UP TO 50% OFF</div><div class="small">Free shipping</div></div>
  </div>
  <div class="promo-tile tile-girl photo" role="img" aria-label="Girl in dark dress standing outdoors">
    <div class="badge-circle"><span class="age">Girl 4 - 16 years</span><span class="big">Shop Now</span></div>
  </div>
</section>

<section class="box" style="top:966px;height:499px">
  <h2 class="box-title" style="top:40px">New Collection</h2>
  <div class="tabs" style="top:100px"><span class="on">Popular</span><span>New Arrivals</span><span>Best Sellers</span></div>
  <div class="product" style="left:47px;top:157px"><div class="pic"><div class="photo" style="background:linear-gradient(#6fc6cf,#3d8fa0)" role="img" aria-label="Teal kids outfit"></div><span class="flag"></span><span class="flag-text">NEW</span></div><div class="name">Sequi Nesciunt</div><div class="stars">★★★★★</div><div class="price"><s>$584.00</s><b>$482.00</b></div></div>
  <div class="product" style="left:247px;top:157px"><div class="pic"><div class="photo" style="background:linear-gradient(#d8dde4,#3a4a6a)" role="img" aria-label="Striped shirt and jeans"></div><span class="flag"></span><span class="flag-text">NEW</span></div><div class="name">Ducimus Qui</div><div class="stars">★★★★★</div><div class="price"><s>$850.00</s><b>$800.00</b></div></div>
  <div class="product" style="left:446px;top:157px"><div class="pic"><div class="photo" style="background:linear-gradient(#f08aa6,#3b4470)" role="img" aria-label="Pink and navy girls dress"></div><span class="flag"></span><span class="flag-text">NEW</span></div><div class="name">Vero Eos</div><div class="stars">★★★★★</div><div class="price"><s>$790.00</s><b>$680.00</b></div></div>
  <div class="product" style="left:642px;top:157px"><div class="pic"><div class="photo" style="background:linear-gradient(#e6e7ec,#9aa1ad)" role="img" aria-label="Checked boys shirt"></div><span class="flag"></span><span class="flag-text">NEW</span></div><div class="name">Vitae Dicta Sunt</div><div class="stars">★★★★★</div><div class="price"><s>$850.00</s><b>$510.00</b></div></div>
  <div class="dots" style="top:430px">• •</div>
</section>

<section class="abs deal">
  <div class="deal-left">
    <div class="deal-copy"><div class="script">Special</div><div class="big">Deal of the week</div><div class="big" style="font-size:36px">Up to 30% off</div><div class="small">On apparel, footwear &amp; more</div></div>
    <div class="countdown">
      <span class="count" style="border-color:#ef8fa9">05</span>
      <span class="count" style="border-color:var(--orange)">06</span>
      <span class="count" style="border-color:var(--teal-dark)">44</span>
      <span class="count" style="border-color:#8fd16f">30</span>
    </div>
    <span class="btn">Shop now</span>
  </div>
  <div class="deal-right photo" role="img" aria-label="Smiling toddler girl sitting on the floor"></div>
  <div class="pill">
    <span class="photo" role="img" aria-label="Baby toy thumbnail"></span>
    <span class="photo" role="img" aria-label="Child portrait thumbnail"></span>
    <span class="photo" role="img" aria-label="Teddy toy thumbnail"></span>
  </div>
</section>

<section class="box" style="top:1866px;height:656px">
  <h2 class="box-title" style="top:44px">Hot Products</h2>
  <p class="box-sub" style="top:82px">Ullam corporis suscipit laboriosam commodi consequatur</p>
  <div class="product" style="left:47px;top:121px"><div class="pic"><div class="photo" style="background:linear-gradient(#e36a4a,#2c3550)" role="img" aria-label="Boys overall set"></div><span class="flag"></span><span class="flag-text">NEW</span></div><div class="name">Sequi Nesciunt</div><div class="stars">★★★★★</div><div class="price"><s>$860.00</s><b>$770.00</b></div></div>
  <div class="product" style="left:247px;top:121px"><div class="pic"><div class="photo" style="background:linear-gradient(#8ac7e8,#e58aa5)" role="img" aria-label="Floral girls dress"></div><span class="flag"></span><span class="flag-text">NEW</span></div><div class="name">Dicta Sunt Explicabo</div><div class="stars">★★★★★</div><div class="price"><s>$500.00</s><b>$480.00</b></div></div>
  <div class="product" style="left:446px;top:121px"><div class="pic"><div class="photo" style="background:linear-gradient(#f1f1f1,#1f2024)" role="img" aria-label="Black suit set"></div><span class="flag"></span><span class="flag-text">NEW</span></div><div class="name">Adipisci Velit</div><div class="stars">★★★★★</div><div class="price"><s>$510.00</s><b>$455.00</b></div></div>
  <div class="product" style="left:642px;top:121px"><div class="pic"><div class="photo" style="background:linear-gradient(#7fa6c7,#c14c48)" role="img" aria-label="Denim dungarees"></div><span class="flag"></span><span class="flag-text">NEW</span></div><div class="name">Qui Dolorem</div><div class="stars">★★★★★</div><div class="price"><s>$650.00</s><b>$520.00</b></div></div>
  <div class="product" style="left:47px;top:393px"><div class="pic"><div class="photo" style="background:linear-gradient(#f7df6a,#e8b93a)" role="img" aria-label="Yellow tulle dress"></div><span class="flag"></span><span class="flag-text">NEW</span></div><div class="name">Porro Quisquam</div><div class="stars">★★★★★</div><div class="price"><s>$540.00</s><b>$488.00</b></div></div>
  <div class="product" style="left:247px;top:393px"><div class="pic"><div class="photo" style="background:linear-gradient(#f07fb0,#c9407e)" role="img" aria-label="Pink winter jacket"></div><span class="flag"></span><span class="flag-text">NEW</span></div><div class="name">Saque Ipsa</div><div class="stars">★★★★★</div><div class="price"><s>$450.00</s><b>$402.00</b></div></div>
  <div class="product" style="left:446px;top:393px"><div class="pic"><div class="photo" style="background:linear-gradient(#54d3b4,#1d9f86)" role="img" aria-label="Mint party dress"></div><span class="flag"></span><span class="flag-text">NEW</span></div><div class="name">Totam Rem</div><div class="stars">★★★★★</div><div class="price"><s>$775.00</s><b>$669.00</b></div></div>
  <div class="product" style="left:642px;top:393px"><div class="pic"><div class="photo" style="background:linear-gradient(#a9cfee,#6b9fd0)" role="img" aria-label="Light blue dress"></div><span class="flag"></span><span class="flag-text">NEW</span></div><div class="name">Rerum Facilis</div><div class="stars">★★★★★</div><div class="price"><s>$350.00</s><b>$280.00</b></div></div>
</section>

<section class="abs newsletter">
  <div class="newsletter-inner"></div>
  <div class="news-title">Subscribe to newsletter</div>
  <div class="news-sub">And get your 20% discount voucher now!</div>
  <div class="news-input">Email address</div>
  <div class="news-btn">SUBSCRIBE</div>
  <div class="news-kid photo" role="img" aria-label="Cheerful boy with glasses giving a thumbs up"></div>
</section>

<section class="box" style="top:2754px;height:311px">
  <h3 class="cat-title">Categories</h3>
  <ul class="cat-list">
    <li><i style="background:var(--teal)"></i>Accessories</li>
    <li><i style="background:var(--purple)"></i>Boys</li>
    <li><i style="background:var(--pink)"></i>Girl</li>
    <li><i style="background:var(--sand)"></i>Kids</li>
    <li><i style="background:var(--orange-deep)"></i>Baby guns</li>
  </ul>
  <span class="arrow" style="left:237px;top:150px">‹</span>
  <div class="product" style="left:251px;top:28px"><div class="pic"><div class="photo" style="background:linear-gradient(#f6b3c6,#e48aa6)" role="img" aria-label="Pink party dress"></div><span class="flag"></span><span class="flag-text">NEW</span></div><div class="name">Quod Maxime</div><div class="stars">★★★★★</div><div class="price"><s>$650.00</s><b>$580.00</b></div></div>
  <div class="product" style="left:448px;top:28px"><div class="pic"><div class="photo" style="background:linear-gradient(#f3c2d2,#8fb4de)" role="img" aria-label="Printed girls dress"></div><span class="flag"></span><span class="flag-text">NEW</span></div><div class="name">Placeat Facere</div><div class="stars">★★★★★</div><div class="price"><s>$545.00</s><b>$380.00</b></div></div>
  <div class="product" style="left:645px;top:28px"><div class="pic"><div class="photo" style="background:linear-gradient(#f2f2f2,#c2282e)" role="img" aria-label="White top with red trousers"></div><span class="flag"></span><span class="flag-text">NEW</span></div><div class="name">Culpa Qui</div><div class="stars">★★★★★</div><div class="price"><s>$460.00</s><b>$380.00</b></div></div>
  <span class="arrow" style="left:843px;top:150px">›</span>
</section>

<section class="box" style="top:3086px;height:487px;border-bottom:none">
  <h2 class="box-title" style="top:50px">Our Blog</h2>
  <p class="box-sub" style="top:92px">Sunt in culpa qui officia deserunt mollit anim id est laborum</p>
  <article class="post" style="left:9px;top:161px">
    <div class="photo" style="background:linear-gradient(150deg,#3b3f8c,#e9e9f0)" role="img" aria-label="Navy lace party dress"></div>
    <h3>Totam rem aperiam eaque ipsa quae ab illo inventore</h3>
    <div class="meta"><span><b>●</b> admin</span><span><b>●</b> 3rd Sept 2017</span></div>
    <p>Sed quia non numquam eius modi tempora incidunt ut labore et dolore magnam quaerat voluptatem aliquam.</p>
  </article>
  <article class="post" style="left:302px;top:161px">
    <div class="photo" style="background:linear-gradient(150deg,#c9c4be,#e56a6a)" role="img" aria-label="Two children standing side by side"></div>
    <h3>Qui in ea voluptate velit esse quam nihil molestiae</h3>
    <div class="meta"><span><b>●</b> admin</span><span><b>●</b> 3rd Sept 2017</span></div>
    <p>Sed quia non numquam eius modi tempora incidunt ut labore et dolore magnam quaerat voluptatem aliquam.</p>
  </article>
  <article class="post" style="left:595px;top:161px">
    <div class="photo" style="background:linear-gradient(150deg,#b9d2e6,#d9b27a)" role="img" aria-label="Toddler playing with toys on a rug"></div>
    <h3>Vel illum qui dolorem eum fugiat quo voluptas nulla pariatur</h3>
    <div class="meta"><span><b>●</b> admin</span><span><b>●</b> 3rd Sept 2017</span></div>
    <p>Sed quia non numquam eius modi tempora incidunt ut labore et dolore magnam quaerat voluptatem aliquam.</p>
  </article>
</section>

<div class="banner photo" style="left:163px;width:284px;background:linear-gradient(160deg,#eae4dc,#c9b7a4)" role="img" aria-label="Girl in white dress holding flowers">
  <div class="banner-copy" style="left:24px;top:120px"><div class="script" style="color:var(--pink)">Girls collections</div><div style="font-size:28px;color:#fff">Up to 50% OFF</div></div>
</div>
<div class="banner photo" style="left:456px;width:286px;background:linear-gradient(180deg,#f0c878,#e8b65c)" role="img" aria-label="Boy playing with a toy car">
  <div class="banner-copy" style="left:20px;top:20px"><div class="script">Child</div><div style="font-size:10px;font-family:'Open Sans',Arial,sans-serif">Accessories Week</div><div style="font-size:28px;line-height:1.1">Up to 50%<br>OFF</div></div>
</div>
<div class="banner photo" style="left:751px;width:286px;background:linear-gradient(160deg,#f3f3f3,#d8343f)" role="img" aria-label="Baby in red snowsuit">
  <span class="abs" style="left:120px;top:262px;background:#2e4f6b;color:#fff;font-family:'Baloo 2',Arial,sans-serif;font-weight:700;font-size:18px;padding:8px 26px">Shop Now</span>
</div>

<section class="abs features">
  <div class="feature" style="left:310px"><svg width="36" height="36" viewBox="0 0 36 36"><rect x="6" y="10" width="24" height="22" rx="3" fill="#e0474c"/><path d="M13 10V7a5 5 0 0 1 10 0v3" fill="none" stroke="#e0474c" stroke-width="2"/><path d="M13 21l4 4 6-7" fill="none" stroke="#fff" stroke-width="2"/></svg><h4>Guarantees</h4><p>Secure orders at every step</p></div>
  <div class="feature" style="left:455px"><svg width="36" height="36" viewBox="0 0 36 36"><rect x="3" y="12" width="20" height="14" fill="#f5a93b"/><path d="M23 16h6l4 5v5H23z" fill="#3fb8b6"/><circle cx="10" cy="28" r="3" fill="#333842"/><circle cx="27" cy="28" r="3" fill="#333842"/></svg><h4>Delivery</h4><p>Free shipping worldwide</p></div>
  <div class="feature" style="left:603px"><svg width="36" height="36" viewBox="0 0 36 36"><rect x="4" y="9" width="28" height="19" rx="3" fill="#6fd0cf"/><rect x="4" y="13" width="28" height="4" fill="#333842"/></svg><h4>Payment</h4><p>Safe and simple checkout</p></div>
  <div class="feature" style="left:745px"><svg width="36" height="36" viewBox="0 0 36 36"><circle cx="18" cy="14" r="9" fill="#f5a93b"/><path d="M12 21l-3 11 9-4 9 4-3-11" fill="#b8a2e3"/></svg><h4>Quality</h4><p>Soft fabrics for little ones</p></div>
</section>

<footer class="abs site-footer">
  <div class="foot-col" style="left:166px;width:210px">
    <div class="brand" style="position:static;margin-bottom:12px"><span class="brand-name" style="font-size:28px">Tulinda</span><span class="brand-dot"></span></div>
    <div style="line-height:1.6">Soft quality clothing for babies and juniors, chosen with care and made to be worn, washed and loved every day.</div>
    <div class="social"><i></i><i></i><i></i><i></i><i></i></div>
  </div>
  <div class="foot-col" style="left:400px">
    <h5 style="color:var(--ink)">Contact us</h5>
    <div>📍 125 Willow Lane, Garden Town</div>
    <div>📞 +(0100) 555-0142</div>
    <div>✉ hello@tulinda.example</div>
  </div>
  <div class="foot-col" style="left:618px">
    <h5 style="color:var(--ink)">Link</h5>
    <div>About</div><div>Track Orders</div><div>Returns</div><div>Shipping</div>
  </div>
  <div class="foot-col" style="left:718px;padding-top:31px">
    <div>Blog</div><div>Wishlist</div><div>Account</div><div>Shipping</div>
  </div>
  <div class="foot-col" style="left:833px">
    <h5 style="color:var(--ink)">Quick contact</h5>
    <div class="foot-field">Name</div>
    <div class="foot-field">Email</div>
    <div class="foot-field" style="height:52px">Message</div>
    <div style="margin-left:130px;width:64px;height:22px;background:var(--orange);color:#fff;font-size:9px;font-weight:700;text-align:center;line-height:22px">SUBMIT</div>
  </div>
  <div class="cards"><i style="background:#c9cfd8"></i><i style="background:#d7dbe2"></i><i style="background:#c9cfd8"></i><i style="background:#d7dbe2"></i></div>
  <div class="chat-btn"><svg width="14" height="12" viewBox="0 0 14 12"><path d="M1 1h12v7H6l-3 3V8H1z" fill="#fff"/></svg>Chat now</div>
</footer>

<div class="abs copyright">©Copyright Information here</div>
<div class="abs to-top"><svg width="12" height="8" viewBox="0 0 12 8"><path d="M1 7l5-5 5 5" fill="none" stroke="#fff" stroke-width="2"/></svg></div>

</body>
</html>
```